Web Design with a Twist! Not cheap design

Please note that this project is ending at 5pm on Tuesday the 28th of September, Australian Western Standard Time!!

Please also note that this project has now been guaranteed!

This project involves three primary elements:
* Logo design;
* Web design - of additional pages and page elements to fit into a site that is already in design/development;
* Graphic design - various images used on the site.

The following materials are included for the project:
* Project requirements
* Company / Site name
* Company / Site description
* Wireframes for new pages / page elements
* Screenshots of existing designs and accompanying definition of constraints for new designs
* PSDs for existing site designs
* Technical requirements for designs
* Content (to guide designs)

Project Requirements:

* Logo design:
This is a new company / site, so we need a new logo. We want to see what you come up with here without giving too much direction that may restrict creativity. If desired, you may find possible guidance through considering the company name, company description, and the existing site designs. Please note that the current logo in the site is for placeholder purposes only.

* Web design:
We need the following pages (and features) to be designed for the site:
• Home page
• Advertise page
• How it works page
We’ve provided some wireframes for the pages, however we definitely don't want you to be guided by the layout/styling at all - the wireframes are only there to indicate the features that we require on each page only. So please ignore all aspects of the wireframes except for the indications of features and functionality.

* Graphic design:
We need various images to be designed throughout the site. These include:
• The image at the top of the ‘Home’ page – please note we will provide some direction on this asap
• The image at the top of the ‘Advertise’ page – please note we will provide some direction n this asap
• The image at the top of the ‘How it Works’ pages
• The images that accompany each of the left hand menu items on the ‘How it Works’ pages (the main images & thumbnails if that’s part of your design). Please note that these images need to be constructed to match the Headlines for each of the ‘What’, ‘Who’, ‘Where’, etc menu items. These Headlines (and some descriptive text) can be found in the Content section at the end of this brief.
• The map of Australia for the ‘Home’ page
• The images to accompany the pricing section of the ‘Advertise’ page
• The variations of the ‘Days on the finder road’ images that are used on the ‘Home’, ‘Advertise’, and ‘How it Works’ pages. Please note that if you want to use different imagery (or no imagery, dependent upon your design) for the Home and Advertise pages then this is your call.

Company Name:
WorkLoom

Company / Site description:
This site will provide a means for contractors ('advertisers') to easily specify and advertise their services, coupled with a means for employers (‘buyers’) to easily seek out and contact these people.
The site will cater for contractor-side advertisements only; job postings will not be accommodated (turning the traditional job advertisement model on its head).
In general, the functionality of the site is somewhat like a mashup of sites like tallowmesh.com and brindlequay.com. The site will incorporate the following primary features of contractor profile display and search, company profile display, (and an availability calendar for v2 release).

Constraints for designs:
On some of the existing designs you will notice that a number of the elements of the site have already been designed. When constructing your designs, please work in accordance with the following constraints:

You have to keep:
• Colour scheme in the header
• Colour scheme in the top navigation buttons (including text colour and background colour)
• Colour scheme for the buttons like on the Register page

You can ignore:
• The existing placeholder logo
• Border, layout, and colour scheme for page elements (like the lines around and inside the register section on the Register page)
• Design of text fields
• Font colour scheme throughout the site – the orange and grey headlines and body text
• Design and colour scheme of the map of Australia
• The breadcrumbs (whether or not they appear, and their layout, styling, colour scheme etc)
• Dropdown styling (assuming you had to make some; currently not on any pages we’re asking you to do) like on the Browse Profession page
• Profile styling (for the home page featured profiles) like on the Browse Profession page
• Footer styling
• Anything else we haven’t explicitly asked you to keep

Technical requirements for design:
Any site designs in either Layered Photoshop files (PSD's) or Illustrator Drawings (AI). RGB Color. Must fit current site design, we work to 1024 wide screens. Usuable area is defined in site designs that are attached in the Photoshop documents; it's around 960px.
Logo work needs to be Illustrator Drawings (AI) and EPS. Need CMYK images for printing and RGB for screen. Logos must include any special fonts that are used as TTF or Open Type. Logos need Color, Monochrome, Reversed and both Tall and Wide usages.

Content for the 'How it Works' pages - this content should guide the images that appear on each page.
* What
Headline: WorkLoom brings contractors and employers together
Descriptive text: (turns the traditional job search model on its head)
* Who
Headline: WorkLoom is for highly skilled professionals and fast moving companies
Descriptive text:
* Where
Headline: Anywhere in Australia, WorkLoom is working by your side
Descriptive text:
* Why
Headline: There are more than 1 million reasons to love WorkLoom
Descriptive text: In Australia, there are 1 million people who work as contractors in their main job, and a further 100,000 people who are contractors in their second job. That’s a lot of contractors!
* When
Headline: WorkLoom is forming partnerships 24 hours a day
Descriptive text:
* How
Headline: Days on the finder road, with WorkLoom
Descriptive text: Advertise on WorkLoom now, and get your days on the finder road.

Remember
Just remember the wireframes we have submitted are just a guide – we want to see your creativity shine. And above all else - have fun!
Thank you.

Please note the deadline for this design competition 5pm on Tuesday the 28th of September, Australian Western Standard Time.

Just under 3 days away!

The deadline of the project will soon be updated to reflect this.

Hi Designers!

Just to be 100% clear about the deadline - the timer is currently showing 7 hours too many. In other words, the project will end 7 hours before the timer finishes.

I will send a notification if the timer starts to display the correct time. So until then, please remember that the deadline is earlier than it seems!

Thanks

Hi Designers,

A couple of really important points:

Firstly - if everyone could please stick to the theme that we provided in the Photoshop files that would be excellent. It is not possible for us to create a new theme. We're dealing with very tight deadlines, so please just provide designs that fit within the current theme.

Secondly, we were really hoping for more illustrations / graphics to be provided in the designs. We're not a fan of the stock photos of generic business people. So please send through designs that incorporate illustrations / graphics for any imagery.

Also just a reminder that this competition is still ending 7 hours earlier than the timer currently displays.

Thanks.

Target Market(s)

The ‘advertiser’ target market for the site is white collar professionals, in all types of industries. The site will be catering for premium contractors only. The site will be catering for both 'in person' contractors, as well as 'knowledge economy' contractors. The site will not be seeking to compete with quorvane.com, pelbix.com, marnoft.com, or similar sites.

The advertiser target market will also encompass companies and labour hire agencies that have contractors in their workforce.

The ‘buyer’ target market will encompass employers, recruitment agents, and member-to-member hiring.

Requirements
Must have
• As per overview
Nice to have
• As per overview
Should not have
• As per overview

```html
<!DOCTYPE html>
<html lang="en">
<head>
<meta charset="utf-8">
<title>WorkLoom – Advertise</title>
<link href="https://fonts.googleapis.com/css2?family=Inter:wght@300;400;600;700;800&display=swap" rel="stylesheet">
<style>
:root{
  --header-top:#5a6677;
  --header-bottom:#7b8695;
  --tab-top:#d2d2d2;
  --tab-bottom:#9a9a9a;
  --tab-active-top:#e0141c;
  --tab-active-bottom:#a80c12;
  --orange:#f06a00;
  --orange-box:#f27312;
  --rule-blue:#3a7fc0;
  --brand-red:#c8102e;
  --cta-top:#c0262c;
  --cta-bottom:#981c21;
  --panel-blue:#2f8cc4;
  --panel-blue-dark:#1b5f93;
  --panel-purple:#9a5a90;
  --panel-purple-dark:#6c3766;
  --headline-grey:#585858;
  --body-grey:#444;
  --footer:#676767;
  --footer-dark:#5c5c5c;
  --footer-text:#cfcfcf;
  --white:#fff;
}
*{box-sizing:border-box;margin:0;padding:0}
html,body{width:1200px;height:1172px;overflow:hidden}
body{position:relative;background:var(--white);font-family:"Inter",Arial,sans-serif;color:var(--body-grey)}
.abs{position:absolute}

.site-header{left:0;top:0;width:1200px;height:156px;background:linear-gradient(var(--header-top),var(--header-bottom))}
.brand{left:143px;top:36px;font-size:50px;font-weight:700;color:var(--brand-red);letter-spacing:-1px}
.utility-links{left:857px;top:26px;font-size:13px;color:#e4e8ee}
.utility-links span{margin:0 12px;opacity:.7}
.main-nav{top:125px;height:31px;display:flex;align-items:center;justify-content:center;color:var(--white);font-size:15px;font-weight:700;border-radius:5px 5px 0 0;background:linear-gradient(var(--tab-top),var(--tab-bottom));border:1px solid #8a8a8a;border-bottom:none}
.main-nav.active{background:linear-gradient(var(--tab-active-top),var(--tab-active-bottom));border-color:#900}

.hero{left:0;top:156px;width:1200px;height:228px;background:var(--orange)}
.hero-rule{left:0;top:384px;width:1200px;height:4px;background:var(--rule-blue)}
.hero-photo{left:211px;top:158px;width:234px;height:226px;background:radial-gradient(ellipse at 50% 35%,#e8c8b0,#5a4a44 60%,#2e2a2a);border-radius:90px 90px 0 0}
.hero-title{left:504px;top:202px;font-size:34px;font-weight:800;line-height:41px;color:var(--white);text-shadow:2px 2px 4px rgba(0,0,0,.55)}
.hero-sub{left:504px;top:287px;font-size:20px;line-height:35px;color:var(--white)}

.intro-title{left:195px;top:420px;font-size:33px;font-weight:700;color:var(--headline-grey);letter-spacing:-.5px}
.intro-body{left:195px;top:458px;width:443px;font-size:13px;line-height:21px}

.how-box{left:670px;top:414px;width:319px;height:233px;background:var(--orange-box)}
.how-title{left:678px;top:422px;font-size:36px;font-weight:300;color:var(--white);letter-spacing:-1px}
.how-body{left:680px;top:470px;width:150px;font-size:14px;line-height:21px;color:var(--white)}
.how-graphic{left:826px;top:469px;width:141px;height:117px;background:linear-gradient(135deg,#cfe3f3,#5c8fbf 55%,#3a5f86);transform:skewY(-6deg)}
.find-btn{left:810px;top:601px;width:162px;height:28px;border-radius:3px;background:linear-gradient(#bdbdbd,#7d7d7d);border:1px solid #e8e8e8;color:var(--white);font-size:13px;display:flex;align-items:center;justify-content:center;letter-spacing:.3px}

.cta{left:188px;width:810px;height:56px;border-radius:8px;background:linear-gradient(var(--cta-top),var(--cta-bottom));border:1px solid #5e1013;display:flex;align-items:center;justify-content:center;color:var(--white);font-size:38px;font-weight:800;text-shadow:2px 2px 3px rgba(0,0,0,.7)}

.pricing-panel{left:185px;top:739px;width:815px;height:202px;border-radius:8px;background:radial-gradient(ellipse at 60% 45%,var(--panel-blue),var(--panel-blue-dark));border:1px solid #123c5e}
.pricing-list{left:195px;top:747px;width:316px;height:187px;border-radius:6px;background:radial-gradient(ellipse at 55% 50%,var(--panel-purple),var(--panel-purple-dark));border:1px solid #e9d3e6}
.plan-photo{left:204px;width:105px;height:61px;background:linear-gradient(135deg,#e8eef4,#9aa8b8 60%,#4a5566)}
.plan-price{left:319px;font-size:22px;font-weight:700;color:var(--white)}
.plan-price small{font-size:14px}
.plan-note{left:319px;font-size:13px;color:#f2e6f0}
.panel-title{left:546px;top:762px;font-size:33px;font-weight:700;color:var(--white);letter-spacing:-.5px}
.panel-body{left:546px;top:801px;width:445px;font-size:13px;line-height:21px;color:var(--white)}

.site-footer{left:0;top:1025px;width:1200px;height:147px;background:repeating-linear-gradient(135deg,var(--footer) 0 3px,var(--footer-dark) 3px 4px)}
.footer-col{top:1041px;font-size:13px;line-height:16.5px;color:var(--footer-text)}
.footer-col b{display:block;color:#bdbdbd;font-weight:700}
.copyright{right:219px;top:1041px;font-size:13px;font-weight:700;color:#c4c4c4}
.social{top:1072px;width:26px;height:26px;border-radius:4px;border:1px solid #3d3d3d}
</style>
</head>
<body>
<header class="abs site-header"></header>
<div class="abs brand">WorkLoom</div>
<div class="abs utility-links">Contact Us<span>|</span>Site Map</div>

<nav>
  <div class="abs main-nav" style="left:360px;width:74px">Home</div>
  <div class="abs main-nav" style="left:438px;width:99px">Find</div>
  <div class="abs main-nav active" style="left:539px;width:101px">Advertise</div>
  <div class="abs main-nav" style="left:642px;width:100px">How it works</div>
  <div class="abs main-nav" style="left:747px;width:98px">Blog</div>
  <div class="abs main-nav" style="left:849px;width:98px">Login</div>
</nav>

<section>
  <div class="abs hero"></div>
  <div class="abs hero-photo" role="img" aria-label="Photo of a smiling professional in a dark blazer"></div>
  <h1 class="abs hero-title">Experienced profrssionals<br>working for you.</h1>
  <p class="abs hero-sub">Aliquipit nis nis ad eriuscil utem vent prationsed el<br>digna alit nonulluptat, venibh exerostie magnaeril ius.</p>
  <div class="abs hero-rule"></div>
</section>

<section>
  <h2 class="abs intro-title">Headline text</h2>
  <p class="abs intro-body">Nostion vulputat. Ip ea feugiatem nulput lum ad tem diam voluptat atismod ignisi endionse eui tie molobor periurem dolore veliquamet aliquis adipis nonsectem ese diam iustis er alisl exerit laor sit vulputet, quamet lor acipsuscidui exer iure et amet, sustis essequi enit incilit venim del ex et amet, con heniat nim quatum eum euip etum nulla facilit, sit, quisim dolorpe rostio con velesecte dolorpe rating et lorer si exer ad dolorerci ex eui tat at. Ut vulla consectem delit alis eu faccum ipit velenibh er irit lutat. Aliquam quatet, se dit lute min euis adit inisi te dolore dolobor senis digna feuisi blandre tionsectem nim ilit at wis aliquipisi.</p>

  <div class="abs how-box"></div>
  <h3 class="abs how-title">How it works</h3>
  <p class="abs how-body">Eessequi enit incilit venim del ex et amet, conquisim dolorpe rostio con velesecte dolorpe rating et lorer si exer ad</p>
  <div class="abs how-graphic" role="img" aria-label="Illustration of a folding world map made of cubes"></div>
  <div class="abs find-btn">FIND OUT NOW</div>
</section>

<div class="abs cta" style="top:669px">CALL TO ACTION - REGISTER NOW</div>

<section>
  <div class="abs pricing-panel"></div>
  <div class="abs pricing-list"></div>
  <div class="abs plan-photo" style="top:766px" role="img" aria-label="Photo of a team of business people"></div>
  <div class="abs plan-price" style="top:770px">$149.95<small>/year</small></div>
  <div class="abs plan-note" style="top:802px">ignisi endionse eui tie molobo</div>
  <div class="abs plan-photo" style="top:852px" role="img" aria-label="Photo of a senior businessman"></div>
  <div class="abs plan-price" style="top:856px">$149.95<small>/year</small></div>
  <div class="abs plan-note" style="top:888px">ignisi endionse eui tie molobo</div>
  <h2 class="abs panel-title">Headline text</h2>
  <p class="abs panel-body">Nostion vulputat. Ip ea feugiatem nulput lum ad tem diam voluptat atismod ignisi endionse eui tie molobor periurem dolore veliquamet aliquis adipis nonsectem ese diam iustis er alisl exerit laor sit vulputet, quamet lor acipsuscidui exer iure et amet, sustis essequi enit incilit venim del ex et amet, con heniat nim quatum eum euip etum nulla facilit, sit, quisim dolorpe rostio</p>
</section>

<div class="abs cta" style="top:953px">CALL TO ACTION - REGISTER NOW</div>

<footer>
  <div class="abs site-footer"></div>
  <div class="abs footer-col" style="left:240px"><b>The Service</b>About<br>Browse<br>Log In</div>
  <div class="abs footer-col" style="left:393px"><b>Support</b>Contact Us<br>FAQ</div>
  <div class="abs footer-col" style="left:537px"><b>Legal</b>Privacy Policy<br>Terms &amp; Conditions</div>
  <div class="abs copyright">2010 TallyWeave Pty Ltd</div>
  <div class="abs social" style="left:841px;background:#1f6fa8" role="img" aria-label="Professional network link"></div>
  <div class="abs social" style="left:879px;background:#3b5a9a" role="img" aria-label="Social network link"></div>
  <div class="abs social" style="left:917px;background:#4fb3d9" role="img" aria-label="Microblog link"></div>
  <div class="abs social" style="left:955px;background:#e8791f" role="img" aria-label="News feed link"></div>
</footer>
</body>
</html>
```